Seminar Invitation for Financial Planning Group

I want a flyer that I can mail out to 5000 people (targeted group of seniors with high incomes and that own homes) to invite to a seminar we will be holding on March 9th and March 10th of 2010. It is a FREE educational workshop and we want to have a colorful catchy flyer that we will be mailing out that doesn't look to cheesy or like a get rich quick scheme. We are experienced financial planners that are proposing long term practical solutions.

Dates and Locations:
March 9th, 2010- Halvern Quastel 5:30 p.m.-7:00 p.m.
March 11th, 2010-Vista Calloway Vineyard 11:00 a.m. -12:30 p.m.

Speakers:
Desmond T. Marquill, ChFC and CLU, focuses on the coordination of insurance, retirement, and estate planning. Des is a member of the Guild of Wealth Advisory Practitioners.
Paul Demontavo, C.F.A., is V.P. of Investment Research at Keystrand Advisory and is a member of the Tremonton Circle of Portfolio Examiners.

Another Speaker:

Social Security Public Relations Director, TBA

At the bottom, it should read, and in similar font as I am posting now:

Desmond T. Marquill is a registered representatie with & securities are offered through Keystrand Advisory, Inc. Member VELTRA/GOBAX CA Insurance License # 0817265 (03-2010)

The font size should be around 12 point

Also, we now have the same of the Social Security Speaker( to go Under Desmond T. Marquill and Paul Demontavo),

Marisol Pennick, San Diego Social Security Public Affairs Specialist

Also, please incorporate at the bottom(the first line and phone number/email should be large compared to the rest of the text so it is easy to locate contact info:

To register, please call (555) 271-9036 or email hilda@marquillbrest.example.

Due to limited capacity, we reserve the right to refuse unregistered guests. Complimentary parking is provided.

CORRECT DATES AND LOCATIONS ARE:
3/9/10 5:30-7:00PM HALVERN QUASTEL
3/10/10 11:00-12:30 P.M. VISTA CALLOWAY LODGE

ALSO ADD, RIGHT ABOVE THE LONG TERM CARE LINE IN THE TOPICS TO BE DISCUSSED SECTION, PLEASE ADD "Top 10 Myths About Social Security" No need for quotation marks I just want to distinguish the text here. Also, I have uploaded 2 pics, one of Paul Demontavo and one of Marisol Pennick. I am still waiting on one from Des Marquill and will post it when I receive it. These are to go to left of their name and short description. 

Target Market(s)

Seniors, People who are about to retire, 55+ in age, primarily those with investable assets of 500k+, those who are concerned with their retirement income and their nest egg.

Industry/Entity Type

Insurance

Requirements
Must have
• An Image(not to make up more than 20% of the flyer). Preferably of a family (elderly couple playing with grandkids, maybe in mid-60''s). Maybe a cartoon of a couple wondering about their financial future since the market tanked and depleted their nest egg.
• -Seminar Dates and Times
• -Must be 1 Page
• -Title of Seminar is "Back to Basics"
• 3 Speakers, each an expert in their field.
• 1)Social Security Speaker 2)Paul Demontavo, CFA, and 3) retirement planning expert, Desmond T. Marquill

• Topics to Be Discussed at Seminar:
• Roth Conversion Pitfalls and Opportunities
• Market Outlook 2010/2011
• How to Maximize Your Retirement Income
• Can You Afford to Not Have Long Term Care?
• And many more....
• Should not have
• No bags of money or bullions. We are not out to have people make a lot of money off of us, we are just advertising good solid financial advice

```html
<!DOCTYPE html>
<html lang="en">
<head>
<meta charset="utf-8">
<title>Back to Basics – Seminar Invitation</title>
<link rel="stylesheet" href="https://fonts.googleapis.com/css2?family=Anton&family=Arimo:wght@700&family=Crimson+Pro:wght@700&family=Goudy+Bookletter+1911&display=swap">
<style>
  :root {
    --maroon: #8a1c1f;
    --orange: #e8923b;
    --forest: #1f4a2c;
    --forest-deep: #173d24;
    --butter: #f5d47f;
    --heading-green: #1d5530;
    --ink: #3a3a3a;
    --white: #ffffff;
  }
  * { margin: 0; padding: 0; box-sizing: border-box; }
  html, body { width: 930px; height: 1200px; overflow: hidden; background: var(--white); }
  .flyer { position: relative; width: 930px; height: 1200px; overflow: hidden; background: var(--white); }

  .family-photo {
    position: absolute; left: 0; top: 172px; width: 930px; height: 1028px;
    background: linear-gradient(180deg, #ffffff 0%, #f6f8f8 14%, #dfe6e9 28%, #c3cfcf 40%, #a9b79e 55%, #8d9a6c 70%, #7c8a5a 85%);
  }
  .swoosh { position: absolute; left: 0; top: 0; width: 930px; height: 1200px; }

  .masthead-band { position: absolute; left: 0; top: 117px; width: 930px; height: 55px; background: var(--orange); }
  .title-lead {
    position: absolute; left: 214px; top: 38px;
    font-family: "Crimson Pro", serif; font-weight: 700; font-size: 66px; line-height: 1;
    color: var(--maroon);
  }
  .title-main {
    position: absolute; left: 488px; top: 10px;
    font-family: "Anton", sans-serif; font-size: 158px; line-height: 1;
    color: var(--white);
    -webkit-text-stroke: 5px var(--orange); paint-order: stroke fill;
    transform: scaleX(0.82); transform-origin: left top;
    letter-spacing: 2px;
  }

  .section-heading {
    position: absolute; font-family: "Arimo", sans-serif; font-weight: 700; font-size: 33px; line-height: 1;
  }
  .topics-heading { left: 28px; top: 198px; color: var(--heading-green); }
  .topics {
    position: absolute; left: 12px; top: 244px; list-style: none;
    font-family: "Goudy Bookletter 1911", serif; font-size: 28px; line-height: 45px; color: var(--ink);
  }
  .topics li { position: relative; padding-left: 33px; }
  .topics li::before {
    content: ""; position: absolute; left: 0; top: 15px; width: 15px; height: 15px;
    border: 3px solid #4f8a3a; border-radius: 50%;
  }

  .speakers-heading { left: 20px; top: 853px; color: var(--butter); }
  .speakers {
    position: absolute; left: 20px; top: 896px; list-style: none;
    font-family: "Goudy Bookletter 1911", serif; font-size: 23px; line-height: 30px; color: var(--white);
  }
  .speakers li { display: flex; }
  .speakers .num { width: 36px; flex: none; }
  .dates-heading { left: 20px; top: 1058px; color: var(--butter); }
  .dates {
    position: absolute; left: 20px; top: 1102px;
    font-family: "Goudy Bookletter 1911", serif; font-size: 22px; line-height: 37px; color: var(--white);
  }
</style>
</head>
<body>
<main class="flyer">
  <div class="family-photo" role="img" aria-label="Photograph of grandparents walking with a toddler grandchild across a grassy hillside"></div>

  <svg class="swoosh" viewBox="0 0 621 801" preserveAspectRatio="none" aria-hidden="true">
    <path d="M285,606 C400,570 510,540 621,522 L621,801 L285,801 Z" fill="var(--butter)"/>
    <path d="M0,418 C55,540 160,612 300,612 C430,612 540,650 621,700 L621,801 L0,801 Z" fill="var(--forest)"/>
  </svg>

  <div class="masthead-band"></div>
  <h1>
    <span class="title-lead">Back to</span>
    <span class="title-main">BASICS</span>
  </h1>

  <h2 class="section-heading topics-heading">Topics to Be Discussed at Seminar:</h2>
  <ul class="topics">
    <li>Roth Conversion Pitfalls and<br>Opportunities</li>
    <li>Market Outlook 2010/2011</li>
    <li>How to Maximize Your Retirement Income</li>
    <li>Can You Afford to Not Have Long Term Care?</li>
    <li>And many more....</li>
  </ul>

  <h2 class="section-heading speakers-heading">Speakers</h2>
  <ol class="speakers">
    <li><span class="num">1)</span><span>&nbsp;Social Security Speaker.</span></li>
    <li><span class="num">2)</span><span>&nbsp;Paul Demontavo. CFA.</span></li>
    <li><span class="num">3)</span><span>Desmond T. Marquill, ChFC<br>and&nbsp;&nbsp;&nbsp; CLU</span></li>
  </ol>

  <h2 class="section-heading dates-heading">Dates and Locations:</h2>
  <p class="dates">
    March 9th, 2010- Halvern Quastel 5:30 p.m.-7:00 p.m.<br>
    March 11th, 2010-Vista Calloway Vineyard 11:00 a.m. -12:30 p.m.
  </p>
</main>
</body>
</html>
```